computter lessons

new business venture [ self employed ] will register my business name as " KEYVORLAN "
what I will offer is :-
computer lessons for new beginners.
Initial set up and basic overview.
lessons per hour in the comfort of your own home.
special rates for customers aged 50+
First lesson is half price with no obligation for booking any further appointments.
a learning and training plan will be presented based on your requirements.
an appraisal update on your new skills.

contact info:-
0161 4970213
07700 900482
larkden@mervoxmail.com

```html
<!DOCTYPE html>
<html lang="en">
<head>
<meta charset="utf-8">
<title>KEYVORLAN – Computer Lessons</title>
<link rel="stylesheet" href="https://fonts.googleapis.com/css2?family=Advent+Pro:wght@200;300&family=Aldrich&family=Roboto+Condensed:wght@700&display=swap">
<style>
  :root {
    --backdrop: #161616;
    --mint: #66bba0;
    --mint-light: #8fd0b9;
    --mint-dark: #4a9c82;
    --teal-text: #5aaf93;
    --label-text: #2f5e50;
    --paper: #f3f3f3;
    --paper-edge: #e2e2e2;
    --white: #ffffff;
  }
  * { box-sizing: border-box; margin: 0; padding: 0; }
  html, body {
    width: 1200px; height: 900px; overflow: hidden;
    background: var(--backdrop);
  }
  .flyer {
    position: absolute; left: 270px; top: 15px;
    width: 614px; height: 866px;
    background: radial-gradient(ellipse at 50% 55%, var(--white) 0%, var(--paper) 60%, var(--paper-edge) 100%);
    overflow: hidden;
  }
  .hero {
    position: absolute; left: 0; top: 0; width: 614px; height: 310px;
    background: linear-gradient(150deg, var(--mint-light) 0%, var(--mint) 55%, var(--mint-dark) 100%);
    border-bottom: 4px solid var(--mint-dark);
  }
  .hero-art {
    position: absolute; left: 240px; top: 30px; width: 360px; height: 250px;
    background: radial-gradient(ellipse at 55% 45%, rgba(255,255,255,0.35) 0%, rgba(255,255,255,0.08) 70%, transparent 100%);
    border-radius: 12px;
  }
  .brand {
    position: absolute; left: 0; top: 237px;
    width: 318px; height: 46px;
    background: rgba(255,255,255,0.18);
    padding-left: 18px;
    font-family: "Advent Pro", sans-serif; font-weight: 200;
    font-size: 44px; line-height: 44px; letter-spacing: 1px;
    color: var(--white);
  }
  .brand span { border-bottom: 1px solid var(--white); padding-bottom: 2px; }
  .features { position: absolute; top: 352px; left: 0; width: 614px; }
  .feature { position: absolute; width: 170px; text-align: center; }
  .feature-icon {
    display: block; margin: 0 auto; width: 109px; height: 109px;
    background: var(--mint);
  }
  .feature-label {
    margin-top: 10px;
    font-family: "Aldrich", sans-serif; font-size: 15px; letter-spacing: 0.3px;
    color: var(--label-text); white-space: nowrap;
  }
  .offer {
    position: absolute; left: 18px; top: 522px; width: 560px; height: 274px;
    border-left: 4px solid var(--mint);
    padding-left: 12px;
    font-family: "Aldrich", sans-serif; font-size: 15px; letter-spacing: 0.3px;
    text-transform: uppercase; color: var(--teal-text);
    white-space: nowrap;
  }
  .offer p { line-height: 23px; }
  .contact {
    position: absolute; left: 0; top: 813px; width: 614px; text-align: center;
    font-family: "Roboto Condensed", sans-serif; font-weight: 700;
    font-size: 12px; line-height: 16px; color: var(--teal-text);
  }
</style>
</head>
<body>
<main class="flyer">
  <header class="hero">
    <div class="hero-art" role="img" aria-label="Flat illustration of a desktop computer, keyboard, light bulb, cloud with gears and a document with pen"></div>
    <h1 class="brand"><span>KEYVORLAN</span></h1>
  </header>

  <section class="features">
    <div class="feature" style="left:25px">
      <svg class="feature-icon" viewBox="0 0 109 109" aria-hidden="true">
        <rect width="109" height="109" fill="#66bba0"/>
        <circle cx="54" cy="54" r="26" fill="none" stroke="#fff" stroke-width="6"/>
        <path d="M50 36 V57 H66" fill="none" stroke="#fff" stroke-width="4"/>
      </svg>
      <p class="feature-label">QUICK SERVICE</p>
    </div>
    <div class="feature" style="left:223px">
      <svg class="feature-icon" viewBox="0 0 109 109" aria-hidden="true">
        <rect width="109" height="109" fill="#66bba0"/>
        <path d="M67 40 C64 32 42 30 42 42 C42 54 68 50 68 64 C68 78 44 76 40 68 M54 24 V86" fill="none" stroke="#fff" stroke-width="3"/>
      </svg>
      <p class="feature-label">SAVE MONEY</p>
    </div>
    <div class="feature" style="left:410px">
      <svg class="feature-icon" viewBox="0 0 109 109" aria-hidden="true">
        <rect width="109" height="109" fill="#66bba0"/>
        <circle cx="26" cy="42" r="10" fill="#fff"/>
        <path d="M12 82 C12 60 40 60 40 82 Z" fill="#fff"/>
        <circle cx="83" cy="42" r="10" fill="#fff"/>
        <path d="M69 82 C69 60 97 60 97 82 Z" fill="#fff"/>
        <circle cx="54" cy="37" r="12" fill="#fff" stroke="#66bba0" stroke-width="2"/>
        <path d="M34 92 C34 56 74 56 74 92 Z" fill="#fff" stroke="#66bba0" stroke-width="2"/>
      </svg>
      <p class="feature-label">FRIENDLY SERVICE</p>
    </div>
  </section>

  <section class="offer">
    <p style="margin-top:24px">Computer lessons for new beginners.</p>
    <p style="margin-top:17px">Initial set up and basic overview.</p>
    <p style="margin-top:16px">Lessons per hour in the comfort of your own home.</p>
    <p style="margin-top:19px">Special rates for customers aged 50+</p>
    <p style="margin-top:16px">First lesson is half price with no obligation for<br>booking any further appointments.A learning and<br>training plan will be presented based on your<br>requirements. An appraisal update on your new skills.</p>
  </section>

  <footer class="contact">
    <p>contact info:- 0161 4970213&nbsp;&nbsp;&nbsp;&nbsp;07700 900482</p>
    <p>larkden@mervoxmail.com</p>
  </footer>
</main>
</body>
</html>
```